OKU professional cleaner

this professional multi-surface cleaner is intended for professionals.
Powerful degreaser. We would like to focus on the professional side.
We already have a range of disinfectants, and we would like a design close to this range but still distinct. The name is OKU and yhe logo is NUVAShine.the visible part of the label is 55mm and will be affixed to a round bottle with trigger .

Target Market(s)

professional

```html
<!DOCTYPE html>
<html lang="en">
<head>
<meta charset="utf-8">
<title>OKU Pro – Professional Multi-Surface Degreaser Label</title>
<link rel="stylesheet" href="https://fonts.googleapis.com/css2?family=Barlow+Condensed:wght@500;600;700&family=Nunito:wght@800&display=swap">
<style>
  :root {
    --page: #f2f3f3;
    --label-white: #fbfbfb;
    --label-grain: #eeeeee;
    --green: #2ea549;
    --green-light: #4fbe64;
    --green-badge: #45b65d;
    --ink: #2b2b2b;
    --ink-soft: #3a3a3a;
    --pill: #d9d9d9;
    --navy: #13304a;
    --teal: #1c5e84;
    --white: #ffffff;
  }
  * { margin: 0; padding: 0; box-sizing: border-box; }
  html, body { width: 1200px; height: 1066px; overflow: hidden; background: var(--page); }
  .canvas { position: relative; width: 1200px; height: 1066px; }

  .label {
    position: absolute; left: 144px; top: 26px; width: 912px; height: 1013px;
    background: linear-gradient(135deg, var(--label-white) 0%, var(--label-grain) 50%, var(--label-white) 100%);
    overflow: hidden;
    box-shadow: 0 2px 14px rgba(0,0,0,0.08);
  }
  .label__tab { position: absolute; left: 125px; top: 0; width: 68px; height: 72px; background: #4a4a4a; }

  .pro-badge {
    position: absolute; left: 92px; top: 85px; width: 142px; height: 142px; border-radius: 50%;
    background: var(--green-badge); color: var(--white);
    display: flex; align-items: center; justify-content: center; text-align: center;
    font-family: "Barlow Condensed", sans-serif; font-weight: 600; font-size: 29px; line-height: 1;
  }

  .brand {
    position: absolute; left: 250px; top: 120px; width: 480px;
    display: flex; align-items: center; justify-content: center; gap: 16px;
  }
  .brand__dot { width: 34px; height: 34px; border-radius: 50%; background: var(--green); }
  .brand__name {
    font-family: "Nunito", sans-serif; font-weight: 800; font-size: 68px; color: var(--green); letter-spacing: -1px;
  }

  .product-name {
    position: absolute; left: 0; right: 0; top: 262px; text-align: center;
    font-family: "Barlow Condensed", sans-serif; font-weight: 700; font-size: 150px; line-height: 1;
    color: var(--ink-soft); letter-spacing: 2px;
  }
  .product-name__accent { color: var(--green); }

  .product-type {
    position: absolute; left: 129px; top: 422px; width: 646px; height: 78px; border-radius: 6px;
    background: var(--pill); color: var(--ink);
    display: flex; align-items: center; justify-content: center;
    font-family: "Barlow Condensed", sans-serif; font-weight: 600; font-size: 56px; letter-spacing: 0.5px;
  }

  .band { position: absolute; left: 0; top: 0; width: 912px; height: 1013px; }

  .formula-seal {
    position: absolute; left: 347px; top: 557px; width: 218px; height: 218px; border-radius: 50%;
    background: radial-gradient(circle, var(--teal) 0 56%, var(--navy) 57% 100%);
    border: 4px solid var(--white);
  }

  .features {
    position: absolute; left: 60px; right: 60px; top: 770px;
    display: flex; justify-content: space-between; align-items: flex-end;
  }
  .feature { display: flex; flex-direction: column; align-items: center; gap: 18px; }
  .feature svg { width: 64px; height: 64px; }
  .feature__text {
    font-family: "Barlow Condensed", sans-serif; font-weight: 500; font-size: 31px; color: var(--white); white-space: nowrap;
  }
  .feature-sep { font-family: "Barlow Condensed", sans-serif; font-size: 32px; color: var(--white); padding-bottom: 2px; }

  .volume {
    position: absolute; left: 299px; top: 938px; width: 306px; height: 75px;
    display: flex; align-items: center; justify-content: center;
    font-family: "Barlow Condensed", sans-serif; font-weight: 600; font-size: 34px; color: var(--ink);
  }
</style>
</head>
<body>
<main class="canvas">
  <section class="label">
    <div class="label__tab"></div>

    <div class="pro-badge">HEAVY<br>DUTY<br>DEGREASER</div>

    <div class="brand">
      <span class="brand__dot"></span>
      <span class="brand__name">NUVAShine</span>
    </div>

    <h1 class="product-name">OKU <span class="product-name__accent">PRO</span></h1>
    <div class="product-type">MULTI-SURFACE DEGREASER</div>

    <svg class="band" viewBox="0 0 912 1013" aria-hidden="true">
      <defs>
        <linearGradient id="bandGreen" x1="0" y1="0" x2="1" y2="0">
          <stop offset="0" stop-color="#2ea549"/>
          <stop offset="0.5" stop-color="#4fbe64"/>
          <stop offset="1" stop-color="#2ea549"/>
        </linearGradient>
      </defs>
      <path d="M0 551 Q456 700 912 524 L912 1013 L0 1013 Z" fill="url(#bandGreen)"/>
      <path d="M0 551 Q456 700 912 524" fill="none" stroke="#13304a" stroke-width="8"/>
      <path d="M299 1013 L317 938 L587 938 L605 1013 Z" fill="#f5f5f5"/>
    </svg>

    <div class="formula-seal" role="img" aria-label="Professional degreasing formula seal"></div>

    <div class="features">
      <div class="feature">
        <svg viewBox="0 0 64 64" fill="none" stroke="#fff" stroke-width="3" stroke-linejoin="round">
          <path d="M32 6 C24 20 14 30 14 42 a18 18 0 0 0 36 0 C50 30 40 20 32 6 Z"/>
          <path d="M20 50 L44 26"/>
        </svg>
        <span class="feature__text">Cuts Grease</span>
      </div>
      <span class="feature-sep">|</span>
      <div class="feature">
        <svg viewBox="0 0 64 64" fill="none" stroke="#fff" stroke-width="3" stroke-linejoin="round">
          <rect x="20" y="28" width="22" height="32" rx="3"/><rect x="24" y="16" width="14" height="12"/>
          <path d="M24 16 H16 V10 H38"/><circle cx="48" cy="12" r="3"/><circle cx="52" cy="22" r="3"/>
        </svg>
        <span class="feature__text">Easy-to-use</span>
      </div>
      <span class="feature-sep">|</span>
      <div class="feature">
        <svg viewBox="0 0 64 64" fill="none" stroke="#fff" stroke-width="3">
          <circle cx="32" cy="34" r="24" stroke-dasharray="6 4"/>
          <text x="32" y="40" text-anchor="middle" fill="#fff" stroke="none" font-family="Barlow Condensed, sans-serif" font-weight="700" font-size="22">5</text>
          <text x="32" y="52" text-anchor="middle" fill="#fff" stroke="none" font-family="Barlow Condensed, sans-serif" font-size="9">MIN</text>
        </svg>
        <span class="feature__text">Fast Action</span>
      </div>
      <span class="feature-sep">|</span>
      <div class="feature">
        <svg viewBox="0 0 64 64" fill="none" stroke="#fff" stroke-width="3" stroke-linejoin="round">
          <rect x="8" y="22" width="48" height="34" rx="4"/>
          <path d="M24 22 V14 H40 V22"/><path d="M8 36 H56"/>
        </svg>
        <span class="feature__text">For Professionals</span>
      </div>
    </div>

    <div class="volume">16.9 FL/500 ML</div>
  </section>
</main>
</body>
</html>
```